Brivan Learning Web Design Project

Who We are:
Brivan Learning is education information portal/ magazine, providing information about the Chinese and International education markets. Our aim is to help school principals improve there curriculum, and parents in understanding this curriculum.

Project Brief:
The site will include education news updates, educational services, curriculum developments and overseas study. We hope the site represents the cross cultural bridge between the west and east. The site will cover both the Sciences and Arts.

Note:
The logo design competition is also underway so we only need the website design

What We want:
This competition is for Design only no coding!
Design a home page based on Template 1,2 or 3. I only need to select one.
The design of an article page.

Optional
Design a Microsoft Windows metro style splash page.

Sites We like:
http://www.qz.com.cn/wordsparrow/default.aspx
http://www.velmaracademicpost.co.uk/
http://pvro.orbalinkstudy.net/

Template Explanations:
Template 1-
The main information has a dynamic sliding category view that when clicked displays the relevant info.
In addition to the main upper menu it also has a left hand sliding menu that pops out on click or gesture

Template 2-
Has limited number of Articles most of the menus are drop downs from the top menu

Template 3-
No Top menu

Target Market(s)

Teachers, principals and parents

Industry/Entity Type

Education

Requirements
Should not have
• kindergarten preschool feel

```html
<!DOCTYPE html>
<html lang="en">
<head>
<meta charset="utf-8">
<title>Brivan Learning</title>
<link href="https://fonts.googleapis.com/css2?family=Ubuntu:wght@300;400;500;700&display=swap" rel="stylesheet">
<style>
:root{
  --navy:#0f3a73;--navy-dark:#0b2a52;--footer-strip:#4a6c96;
  --red:#e2211c;--red-soft:#e0403a;--page:#f4f4f4;--white:#fff;
  --cyan:#29c6f2;--plum:#9b2d5c;--rose:#d94b86;--orange:#e88e2b;
  --pink:#f0167d;--amber:#ea962b;--gold:#f2b84a;--sun:#f4c24e;
  --photo-a:#b9c9d6;--photo-b:#d9b9a0;
}
*{margin:0;padding:0;box-sizing:border-box}
html,body{width:1200px;height:1056px;overflow:hidden}
body{position:relative;background:var(--white);font-family:'Ubuntu',sans-serif;color:var(--navy)}
.abs{position:absolute}
.header{left:0;top:0;width:1200px;height:104px;background:var(--page)}
.brand{left:204px;top:30px;display:flex;align-items:center;gap:10px}
.brand-dot{width:34px;height:34px;border-radius:50%;background:var(--red)}
.brand-name{font-weight:700;font-size:20px;color:var(--navy)}
.call{left:880px;top:22px;display:flex;gap:6px;align-items:center}
.call-label{font-weight:700;font-size:13px;line-height:14px;color:var(--navy)}
.call-num{font-weight:700;font-size:15px;color:var(--red)}
.search{left:804px;top:64px;width:197px;height:26px;background:var(--white);box-shadow:1px 1px 3px rgba(0,0,0,.25);font-size:9px;color:#9aa;padding:8px 13px;font-weight:300}
.search svg{position:absolute;right:6px;top:5px}
.nav{top:104px;height:66px;color:var(--white);font-weight:300;font-size:14px;text-align:center;padding-top:42px;white-space:nowrap}
.nav .ic{position:absolute;left:50%;top:5px;margin-left:-16px;width:32px;height:32px;border-radius:50%;background:rgba(255,255,255,.35);display:flex;align-items:center;justify-content:center}
.nav .ic i{width:20px;height:20px;border-radius:50%;background:rgba(255,255,255,.85)}
.nav .caret{position:absolute;left:50%;bottom:3px;margin-left:-3px;width:6px;height:6px;border-right:1.5px solid #fff;border-bottom:1.5px solid #fff;transform:rotate(45deg) scale(.7)}
.hero{left:200px;top:182px;width:800px;height:348px;background:linear-gradient(120deg,var(--photo-a),var(--photo-b) 50%,#5a6f9a)}
.hl{position:absolute;right:0;background:var(--red-soft);color:var(--white);font-weight:700;font-size:37px;line-height:40px;padding:0 9px;text-align:right;letter-spacing:-.5px;white-space:nowrap}
.dots{left:557px;top:545px;display:flex;gap:4px}
.dots span{width:14px;height:14px;border-radius:50%;border:1px solid #bbb;background:#eee}
.dots span.on{background:var(--navy);border-color:var(--navy)}
.sec-title{font-weight:700;font-size:23px;color:var(--navy);border-bottom:2px dotted var(--navy);padding-bottom:2px;white-space:nowrap}
.card{top:610px;height:156px;background:linear-gradient(160deg,#e8d6c8,#c7b8a9)}
.card-cap{position:absolute;left:0;right:0;bottom:0;height:72px;background:rgba(15,58,115,.82);color:var(--white);padding:7px 10px}
.card-cap h3{font-size:10px;font-weight:500;margin-bottom:2px}
.card-cap p{font-size:9.5px;font-weight:300;line-height:11px}
.card-cap b{font-size:7.5px;font-weight:700}
.card-cap small{display:block;font-size:7.5px}
.card-cap svg{position:absolute;right:8px;bottom:5px}
.connect{left:0;top:774px;width:741px;height:80px;background:var(--red)}
.connect h2{position:absolute;left:202px;top:26px;font-size:22px;line-height:28px;font-weight:700;color:var(--white);white-space:nowrap;letter-spacing:-.5px}
.connect .social{position:absolute;left:423px;top:23px;display:flex;gap:9px}
.connect .social span{flex:none;width:34px;height:34px;border-radius:50%;border:2.5px solid var(--white)}
.news{left:748px;top:610px;width:253px;height:244px;background:var(--navy);padding:10px}
.item{display:flex;gap:8px;height:79px}
.thumb{flex:none;width:90px;height:66px;background:linear-gradient(140deg,#c9b8a4,#7a8ea8)}
.date{display:inline-block;border:1px solid #5b7bad;color:var(--white);font-weight:500;font-size:11px;padding:2px 5px;white-space:nowrap}
.item p{color:#c5d3e8;font-size:9px;line-height:10px;font-weight:300;margin-top:4px}
.item b{display:block;color:var(--white);font-size:7.5px;font-weight:700;margin-top:3px}
.foot-strip{left:0;top:885px;width:1200px;height:11px;background:var(--footer-strip)}
.footer{left:0;top:896px;width:1200px;height:122px;background:var(--navy)}
.fcol{top:14px;color:var(--white)}
.fcol h4{font-size:15px;font-weight:500;margin-bottom:5px;white-space:nowrap}
.fcol a{display:block;color:#dce6f4;font-size:12px;font-weight:300;text-decoration:underline;line-height:18.5px}
.email{width:199px;height:26px;background:var(--white);font-size:9px;color:#8a97a8;padding:8px 15px;margin-top:3px;font-weight:300}
.submit{display:inline-block;background:var(--red);color:var(--white);font-weight:700;font-size:12px;padding:4px 10px;margin-top:6px}
.bottom{left:0;top:1018px;width:1200px;height:38px;background:var(--navy-dark);color:#c9d5e6;font-size:10px;font-weight:300;line-height:38px}
</style>
</head>
<body>
<header class="abs header">
  <div class="abs brand"><span class="brand-dot"></span><span class="brand-name">BRIVAN LEARNING</span></div>
  <div class="abs call">
    <svg width="26" height="28" viewBox="0 0 26 28"><path d="M9 3H4v22h5" fill="none" stroke="#0f3a73" stroke-width="3"/><path d="M10 14h12M17 9l5 5-5 5" fill="none" stroke="#0f3a73" stroke-width="3"/></svg>
    <div><div class="call-label">CALL US NOW</div><div class="call-num">06 5512 0947</div></div>
  </div>
  <div class="abs search">ENTER KEY WORDS
    <svg width="16" height="16" viewBox="0 0 16 16"><circle cx="6.5" cy="6.5" r="4.5" fill="none" stroke="#111" stroke-width="2"/><path d="M10 10l4.5 4.5" stroke="#111" stroke-width="2.5"/></svg>
  </div>
</header>

<nav>
  <div class="abs nav" style="left:200px;width:112px;background:var(--cyan)"><span class="ic"><i></i></span>HOME</div>
  <div class="abs nav" style="left:315px;width:100px;background:var(--plum)"><span class="ic"><i></i></span>ABOUT US<span class="caret"></span></div>
  <div class="abs nav" style="left:418px;width:107px;background:var(--rose)"><span class="ic"><i></i></span>FOR STUDENTS<span class="caret"></span></div>
  <div class="abs nav" style="left:527px;width:72px;background:var(--orange)"><span class="ic"><i></i></span>LESSON<span class="caret"></span></div>
  <div class="abs nav" style="left:602px;width:72px;background:var(--pink)"><span class="ic"><i></i></span>BLOG</div>
  <div class="abs nav" style="left:676px;width:72px;background:var(--amber)"><span class="ic"><i></i></span>JOIN US<span class="caret"></span></div>
  <div class="abs nav" style="left:750px;width:80px;background:var(--gold)"><span class="ic"><i></i></span>CONTACT</div>
  <div class="abs nav" style="left:833px;width:367px;background:var(--sun)"></div>
</nav>

<section class="abs hero" role="img" aria-label="Photo of four smiling students resting their chins on their hands over open books">
  <div class="hl" style="top:188px;height:38px">RAISING</div>
  <div class="hl" style="top:226px;height:38px">THE SKILL LEVELS</div>
  <div class="hl" style="top:264px;height:40px">OF STUDENTS IN HOME</div>
  <div class="hl" style="top:304px;height:44px">CONVENIENC</div>
</section>
<div class="abs dots"><span class="on"></span><span></span><span></span><span></span><span></span></div>

<h2 class="abs sec-title" style="left:200px;top:573px;width:146px">ARTICLES</h2>
<h2 class="abs sec-title" style="left:748px;top:573px;width:164px">LATEST NEWS</h2>

<article class="abs card" style="left:200px;width:218px" role="img" aria-label="Photo of a teacher in glasses with a colleague">
  <div class="card-cap"><h3>LOERM IPSUM DEMANGE.</h3><p>Consectetuer adipiscing elit, sed diam nonummy nibh euismod tincidunt.</p><b>BY : MARLA TENNING</b>
    <svg width="20" height="20" viewBox="0 0 20 20"><circle cx="10" cy="10" r="8.5" fill="none" stroke="#fff" stroke-width="1.5"/><path d="M5 10h9M10 6l4 4-4 4" fill="none" stroke="#fff" stroke-width="1.5"/></svg></div>
</article>
<article class="abs card" style="left:426px;width:315px" role="img" aria-label="Photo of a group of smiling students">
  <div class="card-cap"><h3>LOERM IPSUM DOLLAR</h3><p>Lorem ipsum dolor sit amet, consectetuer adipiscing elit, sed diam nonummy nibh euismod tincidunt ut laoreet.</p><b>BY : OREN FALKE</b><small>29/06/13</small>
    <svg width="20" height="20" viewBox="0 0 20 20"><circle cx="10" cy="10" r="8.5" fill="none" stroke="#fff" stroke-width="1.5"/><path d="M5 10h9M10 6l4 4-4 4" fill="none" stroke="#fff" stroke-width="1.5"/></svg></div>
</article>

<section class="abs connect">
  <h2>CONNECT WITH US :</h2>
  <div class="social"><span></span><span></span><span></span><span></span><span></span><span></span><span></span></div>
</section>

<aside class="abs news">
  <div class="item"><div class="thumb" role="img" aria-label="Photo of a teacher in a classroom"></div><div><span class="date">14 | JULY | 2013</span><p>Lorem ipsum dolor sit amet, consectetuer adipiscing elit,ipsum dolor sit.</p><b>READ MORE</b></div></div>
  <div class="item"><div class="thumb" role="img" aria-label="Photo of students studying at a desk"></div><div><span class="date">14 | JULY | 2013</span><p>Lorem ipsum dolor sit amet, consectetuer adipiscing elit,ipsum dolor sit.</p><b>READ MORE</b></div></div>
  <div class="item"><div class="thumb" role="img" aria-label="Photo of graduates in caps and gowns"></div><div><span class="date">14 | JULY | 2013</span><p>Lorem ipsum dolor sit amet, consectetuer adipiscing elit,ipsum dolor sit.</p><b>READ MORE</b></div></div>
</aside>

<div class="abs foot-strip"></div>
<footer class="abs footer">
  <div class="abs fcol" style="left:202px"><h4>GENERAL</h4><a>HOME</a><a>ABOUT US</a><a>CONTACT US</a><a>CONSULTING</a></div>
  <div class="abs fcol" style="left:372px;top:17px"><h4>NEWS</h4><a>LATEST NEWS</a><a>SUBMIT CONTENT</a></div>
  <div class="abs fcol" style="left:554px;top:17px"><h4 style="margin-left:1px">SUSCRIBE FOR NEWS LETTER</h4><div class="email">YOUR EMAIL ADDERESS</div><span class="submit">SUBMIT</span></div>
  <div class="abs fcol" style="left:826px;top:17px;width:176px;text-align:right"><h4 style="text-align:left;margin-left:35px">CONTACT US</h4>
    <p style="font-size:12px;font-weight:300;line-height:15px;text-align:left;margin-left:35px">ADDRESS : 42 HARLOW LANE, WESTBROOK, OR</p>
    <p style="font-size:10px;font-weight:300;margin-top:6px;white-space:nowrap">MY COPYRIGHT INFO &amp;COPYR; 2013</p></div>
</footer>
<div class="abs bottom"><span style="position:absolute;left:204px">HOME | &nbsp;SITEMAP | &nbsp;CAREERS | &nbsp;CONTACT US | PRIVACY POLICY</span><span style="position:absolute;right:202px">COPYRIGHT © 2013 BRIVAN LEARNING</span></div>
</body>
</html>
```